Website design for a construction company

The logo and the copies of all the 3 pages are attached below. I don't have a preference in colors but I would ideally like to use the colors on my logo, dark teal (secondary) and copper (primary).

Company Name: Corvel Group

Location: London, UK

Business Overview:

Corvel Group is a comprehensive construction company based in London, specializing in a wide range of construction services. We cater to various sectors, providing services including electrical work, painting and decorating, plastering, plumbing, carpentry, kitchen and bathroom installations, loft conversions, and extensions. Our team is known for its skilled craftsmanship, attention to detail, and commitment to quality.

What "CORVEL" stands for:

Our company name, 'CORVEL', is derived from Corvelion, the ancient Greek god of craftsmen, blacksmiths, artisans, sculptors, metals, metallurgy, fire, and volcanoes. Corvelion was renowned in mythology for his incredible skill in crafting and creating, making him the patron of all craftsmen and artisans. His name is synonymous with the mastery of artisanship and the creation of wondrous, enduring works.

In choosing 'CORVEL' as our name, we embody the spirit and skills of Corvelion. It reflects our commitment to craftsmanship, excellence, and durability in the field of construction. Just as Corvelion was known for his meticulous work, precision, and innovative creations, our company strives to uphold these qualities in every project we undertake.

Our name is a constant reminder of our dedication to quality, innovation, and the art of building. It symbolizes our endeavor to achieve the highest standards in construction, much like Corvelion did in his timeless creations. In essence, 'CORVEL' is not just our name; it's a representation of our ethos and the high standards we set for ourselves in the construction industry.

Target Audience:

Our primary audience includes homeowners, real estate developers, and commercial clients in London seeking reliable, high-quality construction services.

Unique Selling Points:

Diverse Range of Services: Offering a one-stop solution for all construction needs.

Certified and Experienced: Professional team with a strong focus on delivering certified and compliant work, particularly in electrical services.

Client-Centric Approach: Emphasizing client satisfaction, we tailor our services to meet the unique needs and visions of our clients.

Quality and Reliability: Commitment to high-quality materials, skilled workmanship, and delivering projects on time and within budget.

Website Requirements:

Clean, professional design reflecting the quality and reliability of our services.

User-friendly navigation to easily access information about our services, portfolio, company background, and contact details.

Portfolio section showcasing our past projects with placeholders for images and descriptions.

Integration of a contact form, map for our location, and links to our social media accounts.

Mobile-responsive design to ensure accessibility across various devices.

Purpose of the Website:
The website aims to:

Establish an online presence and credibility in the construction industry.

Provide an informative resource about our services and past projects to potential clients.

Facilitate easy communication and inquiries through an integrated contact system.

Tone and Style:

Professional, informative, and welcoming. The website should convey trustworthiness and expertise in the construction field.

Target Market(s)

homeowners, real estate developers, and commercial clients

Industry/Entity Type

Construction

Number of Pages Required

3 page

Colors

Designer to choose colors to be used in the design.

```html
<!DOCTYPE html>
<html lang="en">
<head>
<meta charset="utf-8">
<title>Corvel Group — Construction in London</title>
<link href="https://fonts.googleapis.com/css2?family=Roboto:wght@400;500;700;900&family=Open+Sans:wght@400;600&display=swap" rel="stylesheet">
<style>
:root{
  --teal:#1d6d6b;
  --teal-dark:#0e3b3d;
  --teal-deep:#0a2a2c;
  --copper:#b8843a;
  --gold:#c9a048;
  --ink:#1c1c1c;
  --muted:#555;
  --light:#f3f4f4;
  --white:#fff;
  --footer:#101213;
}
*{box-sizing:border-box;margin:0;padding:0}
html,body{width:1200px;height:3584px;overflow:hidden}
body{position:relative;background:var(--white);font-family:"Open Sans",Arial,sans-serif;color:var(--ink)}
.abs{position:absolute}
h1,h2,h3,.nav,.btn{font-family:"Roboto",Arial,sans-serif}
.btn{display:inline-block;color:var(--white);font-size:14px;font-weight:500;padding:12px 24px;border-radius:3px}
.btn-teal{background:var(--teal)}
.btn-copper{background:var(--copper)}

/* header */
.topbar{left:0;top:0;width:1200px;height:72px;background:var(--teal);display:flex;align-items:center;padding:0 60px;justify-content:space-between;z-index:5}
.brand{display:flex;align-items:center;gap:10px;color:var(--white);font-family:"Roboto",sans-serif;font-weight:700;font-size:24px;letter-spacing:1px}
.brand .mark{width:26px;height:26px;background:var(--copper)}
.nav{display:flex;gap:28px;color:var(--white);font-size:14px}
.contact-top{display:flex;gap:20px;align-items:center;color:var(--white);font-size:14px}
.contact-top span{display:flex;align-items:center;gap:6px}

/* hero */
.hero{left:0;top:72px;width:1200px;height:608px;background:linear-gradient(180deg,#2b4f55 0%,#1b3f43 55%,#0e3b3d 100%)}
.hero-photo{left:0;top:0;width:1200px;height:608px;background:linear-gradient(90deg,rgba(14,59,61,.92) 0%,rgba(14,59,61,.55) 60%,rgba(29,109,107,.45) 100%)}
.hero-frame{left:712px;top:96px;width:270px;height:490px;border:3px solid var(--copper);border-radius:14px;background:linear-gradient(180deg,#c6ccd0,#7f8d92)}
.hero-frame-bar{left:726px;top:556px;width:242px;height:24px;background:var(--teal);border-radius:0 0 10px 10px}
.hero h1{left:112px;top:150px;width:590px;color:var(--white);font-size:42px;line-height:52px;font-weight:900;white-space:nowrap;z-index:2}
.hero p{left:112px;top:268px;width:460px;color:var(--white);font-size:18px;line-height:24px;z-index:2}
.hero .btn{left:112px;top:348px;z-index:2}
.badge-card{background:var(--white);border-radius:6px;padding:8px 12px;display:flex;gap:8px;align-items:center;font-size:11px;box-shadow:0 4px 12px rgba(0,0,0,.25);z-index:3}
.badge-card i{width:26px;height:26px;border-radius:50%;background:#b9c3c6;display:block}
.badge-card b{display:block;font-size:12px}
.badge-card em{display:inline-block;margin-top:3px;background:var(--copper);color:#fff;font-style:normal;font-size:9px;padding:2px 6px;border-radius:2px}

/* section titles */
.section-title{display:flex;align-items:center;gap:16px;justify-content:center;font-family:"Roboto",sans-serif;font-weight:700;font-size:36px;color:var(--ink)}
.section-title::before,.section-title::after{content:"";width:80px;height:2px;background:var(--teal)}
.lead{text-align:center;font-size:14px;line-height:21px;color:var(--muted)}

/* about */
.about-bg{left:0;top:700px;width:1200px;height:520px;background:linear-gradient(180deg,#fff,#f4f5f5)}
.about h2{left:180px;top:880px;font-size:38px;font-weight:700;display:flex;align-items:center;gap:14px}
.about h2::after{content:"";width:70px;height:2px;background:var(--teal)}
.about p{left:180px;top:940px;width:440px;font-size:13px;line-height:20px;color:var(--ink)}
.about .btn{left:180px;top:1050px}
.about-photo{left:670px;top:780px;width:350px;height:380px;border:3px solid var(--teal);border-radius:10px;background:linear-gradient(160deg,#cfd6d8,#8fa0a4)}
.play{left:665px;top:860px;width:66px;height:66px;border-radius:50%;background:var(--copper);display:flex;align-items:center;justify-content:center}
.stat{left:700px;top:950px;width:130px;height:130px;border-radius:50%;background:var(--teal);border:4px solid #fff;color:#fff;text-align:center;padding-top:36px;font-family:"Roboto",sans-serif}
.stat b{font-size:34px;display:block}
.stat span{font-size:11px}

/* services */
.services .section-title{left:0;top:1290px;width:1200px}
.services .lead{left:300px;top:1350px;width:600px}
.svc-grid{left:180px;top:1420px;width:840px;display:grid;grid-template-columns:repeat(4,195px);gap:20px 20px}
.svc{height:210px;border-radius:10px;background:linear-gradient(180deg,var(--teal) 0%,#5c7c5b 50%,var(--gold) 100%);color:#fff;text-align:center;padding:24px 16px 0}
.svc .ico{width:70px;height:70px;border-radius:50%;background:#fff;margin:0 auto 14px;display:flex;align-items:center;justify-content:center}
.svc h3{font-size:14px;font-weight:700;margin-bottom:8px;line-height:17px}
.svc p{font-size:10px;line-height:14px}

/* why */
.why-bg{left:0;top:1960px;width:1200px;height:540px;background:linear-gradient(180deg,#f2f3f3,#e8eaea)}
.why-photo{left:120px;top:2000px;width:300px;height:440px;border:3px solid var(--teal);border-radius:10px;background:linear-gradient(180deg,#bfc9cc,#d08a3a 70%,#4f5a5e)}
.why h2{left:592px;top:2070px;font-size:38px;font-weight:700;display:flex;align-items:center;gap:14px}
.why h2::after{content:"";width:70px;height:2px;background:var(--teal)}
.why-list{left:592px;top:2130px;width:470px;list-style:none}
.why-list li{margin-bottom:16px;font-size:12px;line-height:18px;color:var(--muted)}
.why-list li b{display:flex;align-items:center;gap:6px;color:var(--ink);font-size:14px;margin-bottom:4px}
.why .btn{left:592px;top:2380px}

/* testimonial */
.crane{width:140px;height:400px;background:linear-gradient(180deg,rgba(150,160,165,.0),rgba(150,160,165,.18))}
.testi .section-title{left:0;top:2530px;width:1200px}
.testi-card{left:340px;top:2600px;width:520px;height:300px;border:3px solid var(--teal);border-radius:12px;background:#fff;text-align:center;padding:26px 40px 0}
.avatar{width:80px;height:80px;border-radius:50%;margin:0 auto 10px;background:linear-gradient(180deg,#c8b49a,#8a6a4b)}
.stars{color:#17a34a;font-size:20px;letter-spacing:2px;margin-bottom:10px}
.testi-card p{font-size:13px;line-height:20px;color:var(--ink)}
.testi-card small{display:block;margin-top:14px;font-size:12px;color:var(--muted)}
.arrow{width:40px;height:40px;border-radius:50%;border:2px solid var(--ink);display:flex;align-items:center;justify-content:center;background:#fff}

/* cta */
.cta{left:120px;top:2980px;width:960px;height:220px;border-radius:10px;background:linear-gradient(90deg,var(--teal) 0%,#6c7d52 55%,var(--gold) 100%);text-align:center;color:#fff;padding-top:36px}
.cta h2{font-size:30px;line-height:38px;font-weight:700;width:820px;margin:0 auto 22px}
.cta .btn{background:#fff;color:var(--teal);font-size:12px;padding:10px 22px}

/* footer */
.footer{left:0;top:3220px;width:1200px;height:364px;background:var(--footer);color:#ddd}
.footer .brand{position:absolute;left:120px;top:50px;font-size:30px}
.footer .about-txt{position:absolute;left:120px;top:110px;width:240px;font-size:12px;line-height:18px}
.fcol{position:absolute;top:50px}
.fcol h4{font-family:"Roboto",sans-serif;font-size:20px;font-weight:700;color:#fff;margin-bottom:16px}
.fcol ul{list-style:none}
.fcol li{font-size:13px;margin-bottom:10px;display:flex;align-items:center;gap:8px}
.dot{width:18px;height:18px;border-radius:50%;background:var(--copper);display:inline-block;flex:none}
.copy{position:absolute;left:0;bottom:16px;width:1200px;text-align:center;font-size:11px;color:#999;border-top:1px solid #2a2d2e;padding-top:14px}
</style>
</head>
<body>

<header class="topbar abs">
  <div class="brand"><span class="mark"></span>CORVEL</div>
  <nav class="nav"><span>Home</span><span>About Us</span><span>Services</span><span>Projects</span><span>Services</span><span>Blog</span></nav>
  <div class="contact-top">
    <span><svg width="14" height="14" viewBox="0 0 24 24"><path fill="#fff" d="M6.6 10.8a15 15 0 0 0 6.6 6.6l2.2-2.2a1 1 0 0 1 1-.25 11.4 11.4 0 0 0 3.6.57 1 1 0 0 1 1 1V20a1 1 0 0 1-1 1A17 17 0 0 1 3 4a1 1 0 0 1 1-1h3.5a1 1 0 0 1 1 1c0 1.250.2 2.450.57 3.570a1 1 0 0 1-.25 1z"/></svg>123-456-7890</span>
    <span><svg width="14" height="14" viewBox="0 0 24 24"><path fill="#fff" d="M3 5h18v14H3zm2 2v.5l7 4.5 7-4.5V7z"/></svg>info@corvelgroup.com</span>
    <span class="btn btn-copper" style="padding:8px 16px;font-size:12px">Contact Now</span>
  </div>
</header>

<section class="hero abs">
  <div class="hero-photo abs" role="img" aria-label="Construction site skyline behind a teal overlay"></div>
  <div class="hero-frame abs" role="img" aria-label="Construction worker in hard hat and safety vest with arms crossed"></div>
  <div class="hero-frame-bar abs"></div>
  <h1 class="abs">BUILDING YOUR DREAMS<br>INTO REALITY</h1>
  <p class="abs">Expert Craftsmanship Meets Unmatched Reliability in the Heart of London Introduction Section</p>
  <span class="btn btn-teal abs">Get Started</span>
  <div class="badge-card abs" style="left:935px;top:128px"><i></i><div><b>Mara Ellis</b>Site Lead<br><em>Expert</em></div></div>
  <div class="badge-card abs" style="left:716px;top:416px"><i></i><div><b>Mara Ellis</b>Engineer<br><em>Certified</em></div></div>
</section>

<section class="about">
  <div class="about-bg abs"></div>
  <h2 class="abs">ABOUT US</h2>
  <p class="abs">"Welcome to Corvel Group – Where Construction Meets Excellence. Based in London, we are committed to transforming your spaces into exceptional places. Our team is dedicated to delivering the highest quality in every project, attending to every detail with precision and care."</p>
  <span class="btn btn-teal abs">Get Started</span>
  <div class="about-photo abs" role="img" aria-label="Builders reviewing plans on a construction site"></div>
  <div class="play abs"><svg width="22" height="22" viewBox="0 0 24 24"><path fill="#fff" d="M7 4l14 8-14 8z"/></svg></div>
  <div class="stat abs"><b>340+</b><span>Projects Complete</span></div>
</section>

<section class="services">
  <h2 class="section-title abs">OUR SERVICES</h2>
  <p class="lead abs">Tailored to Your Needs: Discover how we can bring your vision to life, covering every aspect of construction from the initial design to the final touches.</p>
  <div class="svc-grid abs">
    <div class="svc"><div class="ico"><svg width="34" height="34" viewBox="0 0 24 24"><path fill="#b8843a" d="M13 2L4 14h6l-1 8 9-12h-6z"/></svg></div><h3>ELECTRICAL WORK</h3><p>Safe certified wiring, lighting and fuse boards fitted to code.</p></div>
    <div class="svc"><div class="ico"><svg width="34" height="34" viewBox="0 0 24 24"><path fill="#b8843a" d="M4 3h14v5H4zM18 5h2v6h-8v3h-2V9h8z"/><rect x="9.5" y="14" width="3" height="7" fill="#1d6d6b"/></svg></div><h3>PAINTING AND DECORATING</h3><p>Clean interior and exterior finishes with lasting colour.</p></div>
    <div class="svc"><div class="ico"><svg width="34" height="34" viewBox="0 0 24 24"><path fill="#b8843a" d="M3 6h14l4 4H3z"/><rect x="9" y="10" width="3" height="10" fill="#1d6d6b"/></svg></div><h3>PLASTERING</h3><p>Smooth walls and ceilings, skimming and full replastering.</p></div>
    <div class="svc"><div class="ico"><svg width="34" height="34" viewBox="0 0 24 24"><path fill="#b8843a" d="M3 8h10v4H7v8H3z"/><path fill="#1d6d6b" d="M13 7h6v6h-2v-2h-4z"/></svg></div><h3>PLUMBING</h3><p>Pipework, boilers and repairs handled quickly and tidily.</p></div>
    <div class="svc"><div class="ico"><svg width="34" height="34" viewBox="0 0 24 24"><path fill="#b8843a" d="M3 17l11-11 4 4L7 21H3z"/><rect x="15" y="3" width="6" height="3" fill="#1d6d6b"/></svg></div><h3>CARPENTRY</h3><p>Bespoke joinery, doors, stairs and fitted storage.</p></div>
    <div class="svc"><div class="ico"><svg width="34" height="34" viewBox="0 0 24 24"><rect x="3" y="11" width="18" height="4" fill="#b8843a"/><path fill="#1d6d6b" d="M5 15h14l-2 5H7zM6 4h3v7H6z"/></svg></div><h3>KITCHEN AND BATHROOM INSTALLATIONS</h3><p>Full fit-outs from design to final tiling.</p></div>
    <div class="svc"><div class="ico"><svg width="34" height="34" viewBox="0 0 24 24"><path fill="#b8843a" d="M12 3l10 9h-3v9H5v-9H2z"/><rect x="10" y="8" width="4" height="4" fill="#fff"/></svg></div><h3>LOFT CONVERSIONS</h3><p>Turn unused roof space into bright living rooms.</p></div>
    <div class="svc"><div class="ico"><svg width="34" height="34" viewBox="0 0 24 24"><path fill="#b8843a" d="M2 11l7-6 7 6v9H2z"/><rect x="16" y="12" width="6" height="8" fill="#1d6d6b"/></svg></div><h3>EXTENSIONS</h3><p>Single and double storey extensions built to last.</p></div>
  </div>
</section>

<section class="why">
  <div class="why-bg abs"></div>
  <div class="why-photo abs" role="img" aria-label="Construction worker in hard hat and orange vest on site"></div>
  <h2 class="abs">WHY CHOOSE US</h2>
  <ul class="why-list abs">
    <li><b><span class="dot" style="width:12px;height:12px;background:var(--teal)"></span>Our Expertise:</b>"Leverage over 15 years of experience. Corvel Group stands as a beacon of excellence in the construction industry. No matter your project, big or small, with exceptional professionalism and skill."</li>
    <li><b><span class="dot" style="width:12px;height:12px;background:var(--teal)"></span>Quality Assurance:</b>"Quality is not just a promise, but a practice. Meticulous attention to detail ensures flawless finishes and durable structures, bringing lasting satisfaction to our clients."</li>
    <li><b><span class="dot" style="width:12px;height:12px;background:var(--teal)"></span>Certified Excellence:</b>"Your safety and satisfaction are our top priorities. We provide electrical certificates and adhere to the highest industry standards, offering peace of mind in every service."</li>
  </ul>
  <span class="btn btn-teal abs">Learn More</span>
</section>

<section class="testi">
  <div class="crane abs" style="left:30px;top:2480px" role="img" aria-label="Faint crane silhouette"></div>
  <div class="crane abs" style="left:1030px;top:2480px" role="img" aria-label="Faint crane silhouette"></div>
  <h2 class="section-title abs">OUR TESTIMONIAL</h2>
  <div class="arrow abs" style="left:170px;top:2820px"><svg width="16" height="16" viewBox="0 0 24 24"><path fill="#1c1c1c" d="M15 4l-8 8 8 8z"/></svg></div>
  <div class="arrow abs" style="left:1010px;top:2820px"><svg width="16" height="16" viewBox="0 0 24 24"><path fill="#1c1c1c" d="M9 4l8 8-8 8z"/></svg></div>
  <div class="testi-card abs">
    <div class="avatar" role="img" aria-label="Client portrait"></div>
    <div class="stars">★★★★★</div>
    <p>"Hear from Our Satisfied Clients: Our commitment to excellence has earned us the trust of numerous homeowners and businesses in London. Read their stories and understand the Corvel Group difference."</p>
    <small>— Lorem Ipsum</small>
  </div>
</section>

<section class="cta abs">
  <h2>"Ready to Start Your Project? Contact us today for a consultation and embark on the journey to turn your construction dreams into a stunning reality."</h2>
  <span class="btn">GET QUOTE</span>
</section>

<footer class="footer abs">
  <div class="brand"><span class="mark"></span>CORVEL</div>
  <p class="about-txt">Corvel Group delivers trusted building work across London, from small repairs to full renovations, with skilled trades and honest pricing on every project.</p>
  <div class="fcol" style="left:420px"><h4>QUICK LINKS</h4><ul><li>Home</li><li>About Us</li><li>Services</li><li>Contact Us</li></ul></div>
  <div class="fcol" style="left:660px"><h4>CONTACT US</h4><ul><li><span class="dot"></span>123-456-7890</li><li><span class="dot"></span>12 Harbour Row, London</li><li><span class="dot"></span>info@corvelgroup.com</li></ul></div>
  <div class="fcol" style="left:900px"><h4>FOLLOW US</h4><ul><li><span class="dot"></span>Community</li><li><span class="dot"></span>Gallery</li><li><span class="dot"></span>Updates</li><li><span class="dot"></span>Network</li></ul></div>
  <div class="copy">Copyright © 2024 Corvel group – All Rights Reserved</div>
</footer>

</body>
</html>
```